Business Card Design for my Real Estate Investing Company

This is for a Real Estate Investing Company that will be serving the Las Vegas Valley. Id like the following slogan included: "Investing in Our Community" I have attached my logo. You will see the color tones I'm interested in..in my logo. I would like the card to be double-sided with a modern, professional look.
Target Market(s)
Homeowners, banks, real estate industry
Industry/Entity Type
Real Estate
Contact Information for Business Card
name: Dale Pruitt
position: Managing Member
address: 4812 Corvane Pkwy ste 207-300
N. Las Vegas, NV 89517
phone: (702) 555-0143
fax: (702) 555-0187
email: OakridgeHousePurchaser@examplemail.com
web: OakridgeHousePurchasers.example
*At the bottom of the card I would like....
We buy houses for cash....no repairs, no commissions, no fees!
Logo Text
OAKRIDGE HOUSE PURCHASERS "Investing in Our Community"
Font styles to use
Other font styles liked:
- Lora
Requirements
Must have
- On the back of the card, i'd like to have my logo large and the following statements:
- Are you considering selling your home? Want a simple, hassle-free transaction? We can help! We buy houses for cash and can close quickly! No need to do any repairs, no realtor commissions, no closing costs.....and no headaches. Let us help you with your real estate needs...!
Nice to have
- multiple colors 2 two tone on front and back

```html
<!DOCTYPE html>
<html lang="en">
<head>
<meta charset="utf-8">
<title>Oakridge House Purchasers – Business Card</title>
<link rel="stylesheet" href="https://fonts.googleapis.com/css2?family=Lora:ital,wght@0,400;0,700;1,700&display=swap">
<style>
  :root {
    --brand-blue: #0b56a4;
    --band-blue: #0a54a0;
    --label-grey: #9a9a9a;
    --title-grey: #5a5a5a;
    --ink: #1a1a1a;
    --band-text: #d8d8d8;
    --paper: #ffffff;
  }
  * { margin: 0; padding: 0; box-sizing: border-box; }
  html, body { width: 1200px; height: 666px; overflow: hidden; background: var(--paper); }
  .card {
    position: relative;
    width: 1200px;
    height: 666px;
    background: var(--paper);
    font-family: "Lora", Georgia, serif;
    overflow: hidden;
  }
  .brand {
    position: absolute;
    top: 62px;
    left: 0;
    width: 100%;
    text-align: center;
  }
  .brand-name {
    display: inline-flex;
    align-items: center;
    gap: 16px;
    font-size: 44px;
    font-weight: 400;
    color: var(--brand-blue);
    letter-spacing: 1px;
  }
  .brand-mark {
    width: 30px;
    height: 30px;
    background: var(--brand-blue);
  }
  .brand-slogan {
    margin-top: 22px;
    font-size: 19px;
    font-style: italic;
    letter-spacing: 7px;
    color: var(--ink);
  }
  .person {
    position: absolute;
    top: 262px;
    left: 0;
    width: 100%;
    text-align: center;
  }
  .person-name {
    font-size: 56px;
    font-weight: 700;
    font-style: italic;
    color: var(--brand-blue);
    line-height: 1.1;
  }
  .person-title {
    font-size: 38px;
    font-weight: 400;
    color: var(--title-grey);
    line-height: 1.2;
  }
  .contact {
    position: absolute;
    top: 476px;
    font-size: 26px;
    line-height: 35px;
    color: var(--brand-blue);
    white-space: nowrap;
  }
  .contact-left { left: 30px; }
  .contact-right { left: 676px; }
  .label { color: var(--label-grey); }
  .offer-band {
    position: absolute;
    left: 0;
    bottom: 0;
    width: 100%;
    height: 66px;
    background: var(--band-blue);
    box-shadow: 0 -4px 5px rgba(0,0,0,0.25);
    text-align: center;
    font-size: 38px;
    line-height: 66px;
    color: var(--band-text);
    white-space: nowrap;
  }
  .offer-band strong { color: var(--paper); font-weight: 700; }
</style>
</head>
<body>
  <div class="card">
    <header class="brand">
      <div class="brand-name"><span class="brand-mark"></span>OAKRIDGE HOUSE PURCHASERS</div>
      <p class="brand-slogan">"Investing in Our Community"</p>
    </header>

    <section class="person">
      <h1 class="person-name">Dale Pruitt</h1>
      <p class="person-title">Managing Member</p>
    </section>

    <address class="contact contact-left" style="font-style:normal">
      <div><span class="label">phone:</span> (702) 555-0143</div>
      <div><span class="label">fax:</span> (702) 555-0187</div>
      <div><span class="label">email:</span> OakridgeHousePurchaser@examplemail.com</div>
    </address>

    <address class="contact contact-right" style="font-style:normal">
      <div><span class="label">adress:</span> 4812 Corvane Pkwy ste 207-300</div>
      <div>N. Las Vegas, NV 89517</div>
      <div><span class="label">web:</span> OakridgeHousePurchasers.example</div>
    </address>

    <footer class="offer-band">We buy houses for <strong>cash</strong> ... no repairs, no commissions, no fees!</footer>
  </div>
</body>
</html>
```